Gutschein-Design für Einzelhandel für Plotterfolien und Zubehör
Zielgruppe
Wir sind ein Einzelhandel für Plotterfolien und Zubehör mitten aus´m Pott.
www.folienfunkelwerk.de
Zur Ansicht einmal die Homepage und unser Fahrzeug
Aufgabenstellung
DIN Lang Quer Datenformat: 216 x 111 mm
Das Format, in dem Ihre Druckdaten angelegt sein sollten. In diesem Format
enthalten sind: 3 mm Beschnitt.
Wir benötigen einen neuen Geschenkgutschein.
Den alten haben wir mit angehangen.
Wir benötigen min. wieder Platz für den
Code
Betrag
Datum

```html
<!DOCTYPE html>
<html lang="de">
<head>
<meta charset="utf-8">
<title>Folienfunkelwerk – Gutschein</title>
<link rel="stylesheet" href="https://fonts.googleapis.com/css2?family=Barlow+Condensed:wght@400&family=Montserrat:wght@400;600;700&display=swap">
<style>
  :root {
    --teal: #2a9aa3;
    --ink: #3b3838;
    --paper: #ffffff;
    --silver: #e3e3e3;
    --skyline: #dcdcdc;
    --band: #4a4949;
    --stage-top: #d4d4d4;
    --stage-bottom: #2a2a2a;
  }
  * { box-sizing: border-box; margin: 0; padding: 0; }
  html, body { width: 1091px; height: 1200px; overflow: hidden; }
  body { font-family: "Montserrat", sans-serif; color: var(--ink); }

  .canvas { position: relative; width: 1091px; height: 1200px; overflow: hidden; background: var(--stage-top); }
  .canvas__lower { position: absolute; left: 0; top: 620px; width: 1091px; height: 580px; background: var(--stage-bottom); }

  .card { position: absolute; width: 522px; height: 268px; background: var(--paper); overflow: hidden; box-shadow: 0 4px 8px rgba(0,0,0,.25); }
  .card--silver { background: var(--silver); }
  .card--brushed { background: linear-gradient(120deg, #f1f1f1 0%, #d9d9d9 55%, #b9b9b9 100%); }

  .card--a { left: 15px; top: 22px; }
  .card--b { left: 560px; top: 22px; }
  .card--c { left: 13px; top: 320px; }
  .card--d { left: 560px; top: 320px; }
  .card--front { left: 15px; top: 780px; }
  .card--back { left: 555px; top: 780px; }

  .brand { display: flex; align-items: center; gap: 10px; }
  .brand__dot { width: 14px; height: 14px; background: var(--teal); flex: none; }
  .brand__name { font-family: "Barlow Condensed", sans-serif; font-weight: 400; font-size: 44px; line-height: 1; color: var(--ink); letter-spacing: .5px; white-space: nowrap; }

  .stack { position: absolute; left: 0; right: 0; display: flex; flex-direction: column; align-items: center; z-index: 1; }
  .label-teal { font-size: 14px; line-height: 1.2; letter-spacing: 1px; color: var(--teal); margin-top: 2px; }

  .skyline { position: absolute; background: linear-gradient(180deg, #e6e6e6, var(--skyline)); }
  .skyline--strip { left: 18px; right: 18px; top: 168px; bottom: 14px; }
  .skyline--narrow { left: 70px; right: 70px; top: 192px; bottom: 14px; }
  .skyline--full { left: 6px; right: 6px; bottom: 18px; height: 215px; background: linear-gradient(180deg, #f7f7f7, #efefef); }

  .lockup-side { position: absolute; left: 80px; top: 60px; width: 385px; }
  .lockup-side__rule { height: 3px; background: var(--teal); margin-top: 14px; }
  .lockup-side__label { font-weight: 700; font-size: 11px; letter-spacing: .5px; text-align: center; margin-top: 6px; }

  .back__brand { position: absolute; left: 232px; top: 30px; }
  .back__brand .brand__name { font-size: 34px; }
  .back__rule { position: absolute; left: 210px; top: 76px; width: 295px; height: 2px; background: var(--teal); }
  .back__tag { position: absolute; left: 300px; top: 86px; background: var(--band); color: #fff; font-weight: 700; font-size: 14px; line-height: 1.4; letter-spacing: 1px; padding: 2px 10px; }

  .field { position: absolute; font-size: 10px; line-height: 1; color: var(--ink); }
  .field__line { position: absolute; height: 1.5px; background: var(--teal); }
  .euro { position: absolute; color: var(--teal); font-weight: 700; font-size: 14px; line-height: 1; }

  .back__band { position: absolute; left: 0; right: 0; top: 158px; height: 70px; background: var(--band); }
  .back__band .skyline { left: 20px; right: 200px; top: 8px; bottom: 6px; background: linear-gradient(180deg, #8d8d8d, #a9a9a9); }
  .back__note { position: absolute; left: 24px; top: 242px; font-size: 10px; line-height: 1; color: var(--ink); white-space: nowrap; }
</style>
</head>
<body>
<main class="canvas">
  <div class="canvas__lower"></div>

  <section class="card card--a">
    <div class="lockup-side">
      <div class="brand"><span class="brand__dot"></span><span class="brand__name">FOLIENFUNKELWERK</span></div>
      <div class="lockup-side__rule"></div>
      <p class="lockup-side__label">GUTSCHEIN</p>
    </div>
    <div class="skyline skyline--strip" role="img" aria-label="Helle Silhouette der Ruhrgebiets-Skyline mit Fördertürmen, Schornsteinen und Windrad"></div>
  </section>

  <section class="card card--b">
    <div class="stack" style="top:118px">
      <div class="brand"><span class="brand__dot"></span><span class="brand__name">FOLIENFUNKELWERK</span></div>
      <p class="label-teal">GUTSCHEIN</p>
    </div>
    <div class="skyline skyline--narrow" role="img" aria-label="Helle Silhouette der Ruhrgebiets-Skyline mit Fördertürmen, Schornsteinen und Windrad"></div>
  </section>

  <section class="card card--c">
    <div class="skyline skyline--full" role="img" aria-label="Große, sehr blasse Silhouette von Industriebauten, Förderturm und Fernsehturm"></div>
    <div class="stack" style="top:120px">
      <div class="brand"><span class="brand__dot"></span><span class="brand__name">FOLIENFUNKELWERK</span></div>
      <p class="label-teal">GUTSCHEIN</p>
    </div>
  </section>

  <section class="card card--d card--silver">
    <div class="stack" style="top:120px">
      <div class="brand"><span class="brand__dot"></span><span class="brand__name">FOLIENFUNKELWERK</span></div>
      <p class="label-teal">GUTSCHEIN</p>
    </div>
  </section>

  <section class="card card--front card--brushed">
    <div class="stack" style="top:112px">
      <div class="brand"><span class="brand__dot"></span><span class="brand__name">FOLIENFUNKELWERK</span></div>
      <p class="label-teal">GUTSCHEIN</p>
    </div>
  </section>

  <section class="card card--back">
    <div class="back__brand brand"><span class="brand__dot"></span><span class="brand__name">FOLIENFUNKELWERK</span></div>
    <div class="back__rule"></div>
    <div class="back__tag">GUTSCHEIN</div>

    <span class="field" style="left:24px;top:48px">Code</span>
    <span class="field__line" style="left:24px;top:64px;width:160px"></span>

    <span class="field" style="left:24px;top:122px">Betrag</span>
    <span class="field__line" style="left:24px;top:140px;width:150px"></span>
    <span class="euro" style="left:180px;top:131px">€</span>

    <span class="field" style="left:230px;top:122px">Datum</span>
    <span class="field__line" style="left:230px;top:140px;width:160px"></span>

    <div class="back__band">
      <div class="skyline" role="img" aria-label="Graue Silhouette der Ruhrgebiets-Skyline mit kleinem Banner"></div>
    </div>

    <p class="back__note">einzulösen beim Folienfunkelwerk - Kastanienallee 24 - 45130 Essen</p>
  </section>
</main>
</body>
</html>
```